Integrated content management graphic

We are looking for a creative iteration for the attached file. We are currently in the process of renewing our branding and this graphic will be a center piece to our product marketing. Our website is www.brelvonvista.com for more information on products and company.
Future projects are available for designers submitting outstanding concepts and branding capability.
Updates

Project Deadline Extended
Reason: We are in the process of picking our final two.

Target Market(s)

Audience is IT and anyone interested in integrating content management with their ERP/Accounting system.

Industry/Entity Type

Construction

Requirements
Must have
• The design must use the current color scheme associated with our website, yellow, black, grey. White can also be used. The design should be sleek.
Nice to have
• 3D Feel. The wheel could take on a stadium concept in 3d.

```html
<!DOCTYPE html>
<html lang="en">
<head>
<meta charset="utf-8">
<title>Integrated Content Management Wheel</title>
<link rel="stylesheet" href="https://fonts.googleapis.com/css2?family=Questrial&display=swap">
<style>
  :root {
    --page-bg: #ffffff;
    --ring-dark: #1c1c1c;
    --ring-mid: #3a3a3a;
    --ring-light: #4a4a4a;
    --divider: #6e6e6e;
    --label: #ffffff;
    --accent: #f2d21b;
  }
  html, body {
    margin: 0;
    padding: 0;
    width: 1200px;
    height: 1200px;
    overflow: hidden;
    background: var(--page-bg);
  }
  .wheel {
    display: block;
    width: 1200px;
    height: 1200px;
  }
  .label {
    font-family: "Questrial", "Century Gothic", sans-serif;
    fill: var(--label);
    letter-spacing: 1px;
  }
  .label--outer { font-size: 44px; }
  .label--middle { font-size: 40px; }
  .label--inner { font-size: 40px; }
  .divider {
    stroke: var(--divider);
    stroke-width: 2;
    fill: none;
  }
  .hub-name {
    font-family: "Questrial", "Century Gothic", sans-serif;
    font-size: 72px;
    fill: var(--accent);
  }
</style>
</head>
<body>
<svg class="wheel" viewBox="0 0 1200 1200" xmlns="http://www.w3.org/2000/svg">
  <defs>
    <filter id="wheel-shadow" x="-10%" y="-10%" width="120%" height="120%">
      <feGaussianBlur in="SourceAlpha" stdDeviation="14"/>
      <feOffset dx="0" dy="4"/>
      <feComponentTransfer><feFuncA type="linear" slope="0.6"/></feComponentTransfer>
      <feMerge><feMergeNode/><feMergeNode in="SourceGraphic"/></feMerge>
    </filter>
    <filter id="label-shadow" x="-20%" y="-40%" width="140%" height="180%">
      <feDropShadow dx="2" dy="3" stdDeviation="2" flood-color="#000" flood-opacity="0.9"/>
    </filter>
    <radialGradient id="ring-outer" cx="600" cy="600" r="570" gradientUnits="userSpaceOnUse">
      <stop offset="0.69" stop-color="#222"/>
      <stop offset="0.8" stop-color="#3d3d3d"/>
      <stop offset="0.95" stop-color="#353535"/>
      <stop offset="1" stop-color="#1e1e1e"/>
    </radialGradient>
    <radialGradient id="ring-middle" cx="600" cy="600" r="395" gradientUnits="userSpaceOnUse">
      <stop offset="0.58" stop-color="#1a1a1a"/>
      <stop offset="0.75" stop-color="#333"/>
      <stop offset="0.95" stop-color="#3b3b3b"/>
      <stop offset="1" stop-color="#202020"/>
    </radialGradient>
    <radialGradient id="ring-inner" cx="600" cy="600" r="232" gradientUnits="userSpaceOnUse">
      <stop offset="0.36" stop-color="#111"/>
      <stop offset="0.6" stop-color="#262626"/>
      <stop offset="0.93" stop-color="#3a3a3a"/>
      <stop offset="1" stop-color="#1c1c1c"/>
    </radialGradient>
    <radialGradient id="hub-ball" cx="575" cy="560" r="110" gradientUnits="userSpaceOnUse">
      <stop offset="0" stop-color="#5a5a5a"/>
      <stop offset="0.45" stop-color="#1d1d1d"/>
      <stop offset="1" stop-color="#050505"/>
    </radialGradient>

    <path id="arc-accounting" d="M 138,600 A 462 462 0 0 1 1062,600"/>
    <path id="arc-office" d="M 298,600 A 302 302 0 0 1 902,600"/>
    <path id="arc-capture" d="M 446,600 A 154 154 0 0 1 754,600"/>
    <path id="arc-workflow" d="M 430,600 A 170 170 0 0 0 770,600"/>
    <path id="arc-project" d="M 325,600 A 275 275 0 0 0 875,600"/>
    <path id="arc-software" d="M 278,600 A 322 322 0 0 0 922,600"/>
    <path id="arc-equipment" d="M 130,600 A 470 470 0 0 0 1070,600"/>
  </defs>

  <g class="wheel-body" filter="url(#wheel-shadow)">
    <circle class="ring ring--outer" cx="600" cy="600" r="570" fill="url(#ring-outer)"/>
    <circle class="ring ring--middle" cx="600" cy="600" r="395" fill="url(#ring-middle)"/>
    <circle class="ring ring--inner" cx="600" cy="600" r="232" fill="url(#ring-inner)"/>
  </g>

  <g class="dividers">
    <circle class="divider" cx="600" cy="600" r="395"/>
    <circle class="divider" cx="600" cy="600" r="232"/>
    <line class="divider" x1="197" y1="197" x2="540" y2="540"/>
    <line class="divider" x1="1003" y1="197" x2="660" y2="540"/>
    <line class="divider" x1="197" y1="1003" x2="540" y2="660"/>
    <line class="divider" x1="1003" y1="1003" x2="660" y2="660"/>
  </g>

  <g class="labels" filter="url(#label-shadow)">
    <text class="label label--outer"><textPath href="#arc-accounting" startOffset="50%" text-anchor="middle">Accounting</textPath></text>
    <text class="label label--outer"><textPath href="#arc-equipment" startOffset="50%" text-anchor="middle" dominant-baseline="hanging">Equipament Mgmt</textPath></text>
    <text class="label label--outer" transform="translate(175 600) rotate(-90)" text-anchor="middle">Property Mgmt</text>
    <text class="label label--outer" transform="translate(1072 600) rotate(-90)" text-anchor="middle">Facilities Mgmt</text>

    <text class="label label--middle"><textPath href="#arc-office" startOffset="50%" text-anchor="middle">Suite Office</textPath></text>
    <text class="label label--middle"><textPath href="#arc-project" startOffset="50%" text-anchor="middle" dominant-baseline="hanging">Project</textPath></text>
    <text class="label label--middle"><textPath href="#arc-software" startOffset="50%" text-anchor="middle" dominant-baseline="hanging">Mgmt Software</textPath></text>
    <text class="label label--middle" transform="translate(305 605) rotate(-90)" text-anchor="middle">TeamPortal</text>
    <text class="label label--middle" transform="translate(875 600) rotate(-90)" text-anchor="middle">Document</text>
    <text class="label label--middle" transform="translate(935 600) rotate(-90)" text-anchor="middle">Management</text>

    <text class="label label--inner"><textPath href="#arc-capture" startOffset="50%" text-anchor="middle">Capture</textPath></text>
    <text class="label label--inner"><textPath href="#arc-workflow" startOffset="50%" text-anchor="middle" dominant-baseline="hanging">Workflow</textPath></text>
    <text class="label label--inner" transform="translate(453 598) rotate(-90)" text-anchor="middle">Archiving</text>
    <text class="label label--inner" transform="translate(784 600) rotate(-90)" text-anchor="middle">ERP</text>
  </g>

  <g class="hub">
    <circle cx="600" cy="600" r="86" fill="#2a2a2a" stroke="#555" stroke-width="2"/>
    <circle cx="600" cy="600" r="74" fill="url(#hub-ball)"/>
    <text class="hub-name" x="600" y="626" text-anchor="middle">BV</text>
  </g>
</svg>
</body>
</html>
```